Web Design Project for new Anaesthetic Pracitice

We have recently obtained our brand new logo from PixelHarbor and now it's time to move on to our website. We are a new anaesthetic practice that offers state of the art anaesthesia care.

We are after a design that communicates professionalism, along with a modern, forward thinking attitude.

Reason: I would like the chance to see more designs. I have also increased the budget and will be providing a little more guidance on required elements.

I have just increased the budget on this project.  $400 for first place, $100 for second.

Also view the brief for some further guidance to help refine designs

Reason: As our deadline is now almost upon us and we have only just sorted out the issues with our increased budget I thought it only fair to give other designers a chance to see if they wish to participate. As a consolation to you all the project is now guaranteed.

Target Market(s)

Our patients and to a lesser extent the surgeons we work with

Requirements
Must have
• The same clean, sleek modern look that we have in our logo. The logo should feature prominently (examples are uploaded)

Menu system, either vertical or horizontal.
The menu system will include the following:
• Home
• Our People
• Our Hospitals
• Our Charges
• Booking Form
• Patient Information
• Contact Information

If designers think they can find more succinct wording for these categories they are free to try.

Some of these menu entries will in all probability lead to a drop down menu (Or People, Our Hospitals and Patient Information in particular). Consideration to how these menus will look and what they are likely to cover is a must.

If your design is selected you will be asked to produce a PSD for both the main page and for any secondary pages (which will be a development of the main page, with the same basic layout, just with a single lot of content) unless your design is one where all pages on the site look the same (i.e. the main page does not have portions of the other pages or leaders on it)

Design delivered as a layered PSD file so we can have our coders chop and slice it into a CSS website.

Use of the logo as uploaded below

A space reserved for breadcrumbs.

Use of the TrustVane logo, preferably in the footer, but we will accept it at the bottom of a side bar. Examples are included below.

The font in the logo is Sommet. We have the ability to install this as a webfont, feel free to utilise it in the site if you so wish.

Contact information can be either a menu option or in the footer.

Nice to have
• Rotating images (either provide us with dummies or just blank placeholder spaces, we have an in-house professional photographer who will be able to populate any such area)

Either a design with all pages on the site looking the same or with a main home page and a separate, related design for other pages (the full site will have about 30 pages, covering how to get to the office, how to get to the hospitals we work at (with roamly charts), the doctors working for us, our office staff, some information on why we charge what we do, and a range of patient information pages)

Icons for Chatterly and Blipster. We have no need for Vid Nest, Pokk, Snapro or Murmo right now, but if you want to include icons for these, feel free, we can always use them later.

These sort of icons can be placed anywhere but personally I like them in the footer.

A footer menu is not mandatory but if it works better with your design feel free to do so.
Should not have
• Pictures of young doctors in white coats, stethoscopes, cadeucus (staff and serpent), all are clichéd and worn out.

```html
<!DOCTYPE html>
<html lang="en">
<head>
<meta charset="utf-8">
<title>Ridgeway Plains Anaesthetic Specialists</title>
<link href="https://fonts.googleapis.com/css2?family=PT+Sans:wght@400;700&family=Arimo:wght@400&display=swap" rel="stylesheet">
<style>
  :root{
    --red:#e0141e;
    --red-dark:#b70f18;
    --black:#000;
    --ink:#444;
    --heading:#4a4a4a;
    --panel:#f7f7f7;
    --panel-line:#dedede;
    --white:#fff;
    --hero-deep:#0b2a63;
    --hero-mid:#2e63b8;
    --hero-light:#9fd0f4;
  }
  *{margin:0;padding:0;box-sizing:border-box;}
  html,body{width:1074px;height:1200px;overflow:hidden;}
  body{position:relative;background:linear-gradient(#fff 490px,#f8f8f8 800px,#efefef 1134px);font-family:"Arimo",Arial,sans-serif;color:var(--ink);}
  .site-header{position:absolute;left:0;top:0;width:1074px;height:93px;background:var(--white);}
  .brand{position:absolute;left:132px;top:26px;display:flex;align-items:center;gap:12px;}
  .brand-dot{width:28px;height:28px;border-radius:50%;background:var(--red);}
  .brand-name{font-family:"PT Sans",sans-serif;font-size:15px;line-height:17px;color:#333;font-weight:400;}
  .follow{position:absolute;right:150px;top:40px;display:flex;align-items:center;gap:10px;font-family:"PT Sans",sans-serif;font-size:13px;font-weight:700;color:#111;}
  .follow .social{display:flex;align-items:center;gap:4px;font-weight:400;font-size:11px;color:#333;}
  .follow .social span.dot{width:14px;height:14px;border-radius:50%;}
  .dot-chat{background:#3b5998;}
  .dot-blip{background:#2aa9e0;}
  .red-band{position:absolute;left:0;top:93px;width:1074px;height:389px;background:var(--red);}
  .main-nav{position:absolute;left:133px;top:103px;width:806px;height:37px;background:var(--black);border-radius:3px;display:flex;align-items:center;justify-content:space-around;padding:0 14px;}
  .main-nav a{color:var(--white);text-decoration:none;font-family:"PT Sans",sans-serif;font-weight:700;font-size:11px;letter-spacing:.2px;}
  .hero{position:absolute;left:133px;top:154px;width:806px;height:307px;background:var(--white);padding:8px;}
  .hero-image{width:100%;height:100%;background:radial-gradient(ellipse at 52% 45%,var(--hero-light) 0%,var(--hero-mid) 35%,var(--hero-deep) 80%);}
  .slider-dots{position:absolute;left:0;right:0;bottom:12px;display:flex;justify-content:center;gap:6px;}
  .slider-dots span{width:11px;height:11px;border-radius:50%;background:var(--white);}
  .slider-dots span.active{background:var(--red-dark);}
  .breadcrumb{position:absolute;left:135px;top:465px;font-family:"PT Sans",sans-serif;font-size:10px;line-height:12px;color:var(--white);}
  .breadcrumb a{color:var(--white);text-decoration:none;}
  .panel{position:absolute;top:502px;width:393px;height:264px;background:var(--panel);border:1px solid var(--panel-line);}
  .panel h2{font-family:"PT Sans",sans-serif;font-weight:400;font-size:20px;color:var(--heading);padding:8px 10px 6px;border-bottom:1px solid var(--panel-line);}
  .panel-body{padding:10px 8px 0;font-size:9.5px;line-height:15px;text-align:justify;}
  .panel-body p{margin-bottom:15px;}
  .panel-body .lead{color:var(--red);font-size:11px;line-height:15px;text-align:left;}
  .welcome{left:134px;}
  .speciality{left:545px;}
  .speciality .panel-body p{margin-bottom:10px;}
  .checklist{list-style:none;padding-left:12px;}
  .checklist li{display:flex;align-items:center;gap:12px;height:25px;}
  .feature{position:absolute;top:780px;width:253px;height:340px;}
  .feature h3{font-family:"PT Sans",sans-serif;font-weight:700;font-size:15px;color:var(--heading);height:36px;line-height:20px;}
  .feature-image{height:114px;}
  .feature p{font-size:9.5px;line-height:15px;text-align:justify;margin-top:15px;margin-left:-2px;}
  .more{position:absolute;top:313px;left:0;width:68px;height:24px;background:var(--black);color:var(--white);font-family:"PT Sans",sans-serif;font-size:13px;text-align:center;line-height:24px;text-decoration:none;}
  .f1{left:134px;} .f2{left:411px;} .f3{left:688px;}
  .img-tools{background:linear-gradient(120deg,#dfe9f2,#9fb8cf 55%,#e9eef2);}
  .img-team{background:linear-gradient(120deg,#6d7b86,#b9c6d0 50%,#7a8a96);}
  .img-patient{background:linear-gradient(120deg,#b7cde0,#e9dccb 50%,#8ebbd9);}
  .site-footer{position:absolute;left:0;top:1134px;width:1074px;height:66px;background:var(--black);}
  .copyright{position:absolute;left:135px;top:27px;color:var(--white);font-family:"PT Sans",sans-serif;font-weight:700;font-size:9px;}
  .trust-badge{position:absolute;left:842px;top:9px;width:89px;height:49px;background:var(--white);border-radius:3px;border-bottom:9px solid var(--red-dark);}
</style>
</head>
<body>
  <header class="site-header">
    <div class="brand">
      <span class="brand-dot"></span>
      <span class="brand-name">Ridgeway Plains<br>Anaesthetic Specialists</span>
    </div>
    <div class="follow">
      Follow Us:
      <span class="social"><span class="dot dot-chat"></span>Chatterly</span>
      <span class="social"><span class="dot dot-blip"></span>Blipster</span>
    </div>
  </header>

  <div class="red-band"></div>

  <nav class="main-nav">
    <a href="#">HOME</a>
    <a href="#">OUR PEOPLE</a>
    <a href="#">OUR HOSPITALS</a>
    <a href="#">OUR CHARGES</a>
    <a href="#">BOOKING FORM</a>
    <a href="#">PATIENT INFORMATION</a>
    <a href="#">CONTACT</a>
  </nav>

  <section class="hero">
    <div class="hero-image" role="img" aria-label="Modern operating theatre bathed in blue light with glowing light streaks over the table"></div>
    <div class="slider-dots"><span class="active"></span><span></span><span></span><span></span></div>
  </section>

  <nav class="breadcrumb" aria-label="Breadcrumb"><a href="#">Home</a> &rsaquo; Welcome</nav>

  <section class="panel welcome">
    <h2>Welcome</h2>
    <div class="panel-body">
      <p class="lead">ed ut perspiciatis unde omnis iste natus error sit voluptatem accusantium doloremque laudantium,</p>
      <p>totam rem aperiam, eaque ipsa quae ab illo inventore veritatis et quasi architecto beatae vitae dicta sunt explicabo. Nemo enim ipsam voluptatem quia voluptas sit aspernatur aut odit aut fugit, sed quia consequuntur magni dolores eos qui ratione voluptatem sequi nesciunt.</p>
      <p>Neque porro quisquam est, qui dolorem ipsum quia dolor sit amet, consectetur, adipisci velit, sed quia non numquam eius modi tempora incidunt ut labore et dolore magnam aliquam quaerat voluptatem. Ut enim ad minima veniam, quis nostrum exercitationem ullam corporis suscipit laboriosam, nisi ut aliquid ex ea commodi consequatur? Quis autem vel eum iure reprehenderit qui in ea voluptate velit esse quam nihil molestiae consequatur,</p>
    </div>
  </section>

  <section class="panel speciality">
    <h2>Our Speciality</h2>
    <div class="panel-body">
      <p>totam rem aperiam, eaque ipsa quae ab illo inventore veritatis et quasi architecto beatae vitae dicta sunt explicabo. Nemo enim ipsam voluptatem quia voluptas sit aspernatur aut odit aut fugit, sed quia consequuntur magni dolores eos qui ratione voluptatem sequi nesciunt.aspernatur aut odit aut fugit, sed quia consequuntur magni dolores eos qui ratione voluptatem sequi nesciunt.</p>
      <ul class="checklist">
        <li><svg width="10" height="9" viewBox="0 0 10 9"><path d="M1 5 L4 8 L9 1" fill="none" stroke="#e0141e" stroke-width="2"/></svg>Neque porro quisquam est, qui</li>
        <li><svg width="10" height="9" viewBox="0 0 10 9"><path d="M1 5 L4 8 L9 1" fill="none" stroke="#e0141e" stroke-width="2"/></svg>dolorem ipsum quia dolor sit amet</li>
        <li><svg width="10" height="9" viewBox="0 0 10 9"><path d="M1 5 L4 8 L9 1" fill="none" stroke="#e0141e" stroke-width="2"/></svg>consectetur, adipisci velit, sed quia</li>
        <li><svg width="10" height="9" viewBox="0 0 10 9"><path d="M1 5 L4 8 L9 1" fill="none" stroke="#e0141e" stroke-width="2"/></svg>on numquam eius modi tempora incidunt</li>
        <li><svg width="10" height="9" viewBox="0 0 10 9"><path d="M1 5 L4 8 L9 1" fill="none" stroke="#e0141e" stroke-width="2"/></svg>ut labore et dolore magnam</li>
      </ul>
    </div>
  </section>

  <section class="feature f1">
    <h3>How does it work?</h3>
    <div class="feature-image img-tools" role="img" aria-label="Gloved hand holding a surgical instrument"></div>
    <p>Neque porro quisquam est, qui dolorem ipsum quia dolor sit amet, consectetur, adipisci velit, sed quia non numquam eius modi tempora incidunt ut labore et dolore magnam aliquam quaerat voluptatem.</p>
    <p>Ut enim ad minima veniam, quis nostrum exercitationem ullam corporis suscipit laboriosam, nisi ut aliquid ex ea commodi consequatur? Quis autem vel eum iure repre-henderit qui in ea voluptate velit esse quam nihil moles-</p>
    <a class="more" href="#">MORE</a>
  </section>

  <section class="feature f2">
    <h3>Who We Are?</h3>
    <div class="feature-image img-team" role="img" aria-label="Anaesthetist in surgical cap and mask in theatre"></div>
    <p>Neque porro quisquam est, qui dolorem ipsum quia dolor sit amet, consectetur, adipisci velit, sed quia non numquam eius modi tempora incidunt ut labore et dolore magnam aliquam quaerat voluptatem.</p>
    <p>Ut enim ad minima veniam, quis nostrum exercitationem ullam corporis suscipit laboriosam, nisi ut aliquid ex ea commodi consequatur? Quis autem vel eum iure repre-henderit qui in ea voluptate velit esse quam nihil moles-</p>
    <a class="more" href="#">MORE</a>
  </section>

  <section class="feature f3">
    <h3>Services</h3>
    <div class="feature-image img-patient" role="img" aria-label="Clinician preparing an injection beside a patient"></div>
    <p>Neque porro quisquam est, qui dolorem ipsum quia dolor sit amet, consectetur, adipisci velit, sed quia non numquam eius modi tempora incidunt ut labore et dolore magnam aliquam quaerat voluptatem.</p>
    <p>Ut enim ad minima veniam, quis nostrum exercitationem ullam corporis suscipit laboriosam, nisi ut aliquid ex ea commodi consequatur? Quis autem vel eum iure repre-henderit qui in ea voluptate velit esse quam nihil moles-</p>
    <a class="more" href="#">MORE</a>
  </section>

  <footer class="site-footer">
    <p class="copyright">©2012 Ridgeway Plains Anaesthetic Specialists.</p>
    <div class="trust-badge" aria-label="TrustVane security badge"></div>
  </footer>
</body>
</html>
```